New Body Mist 250 ml exclusive

We are excited to embark on a new project to design the packaging for body mist:
Amber Drizzle

We are looking for a design that is truly unique and stands out, with a touch of individuality that sets it apart. The design should be eye-catching and visually appealing, drawing attention even from a distance. We want the body mists to have a fun and attractive look that appeals to customers.

To help bring your design to life, we will provide the dimensions of the bottle, which has a capacity of 250ml. The bottle measures 13.3 cm in height and 4.9 cm in diameter (excluding the pump). Additionally, we will also provide the dimensions of the label, which measures 15.1 cm in height and 12.8 cm in width.

We believe that giving you the freedom to put your own unique touch and color choices will help create a truly standout design. We look forward to seeing your creative vision for our body mist.

We shared with you the logo of the body mist and some examples of models that we liked.

Please be informed that the project only includes one design and the remaining three will be completed and paid for through a 1on1 project with the winner of the contest.

Target Market(s)

Supermarket and perfumery stores

Industry/Entity Type

Cosmetics

Font styles to use
Serif

Requirements
Must have
• Uniqueness and attractiveness

```html
<!DOCTYPE html>
<html lang="en">
<head>
<meta charset="utf-8">
<title>Amber Drizzle – Body Mist Labels</title>
<link href="https://fonts.googleapis.com/css2?family=Montserrat:wght@300;400;500&family=Oswald:wght@200;300&display=swap" rel="stylesheet">
<style>
  :root {
    --page: #ffffff;
    --white: #ffffff;
    --bloom-base: #f21fe0;
    --bloom-light: #ff3cf0;
    --bloom-box: #ff10b4;
    --bloom-flower: #e0147a;
    --bloom-flower-soft: #ff5fb8;
    --tide-deep: #1474c4;
    --tide-mid: #22a9dc;
    --tide-light: #3fd3dc;
    --tide-green: #b9e0b0;
    --tide-box: #0b68c4;
    --orchid: #e6dcf0;
    --orchid-soft: #b79ad0;
    --lily: #e8b8e4;
  }
  * { margin: 0; padding: 0; box-sizing: border-box; }
  html, body { width: 1200px; height: 1200px; overflow: hidden; background: var(--page); }
  .sheet {
    position: relative; width: 1200px; height: 1200px;
    display: flex; justify-content: center; align-items: center; gap: 100px;
  }
  .label {
    position: relative; width: 360px; height: 950px; overflow: hidden;
    color: var(--white);
  }
  .label--bloom { background: linear-gradient(180deg, var(--bloom-light) 0%, var(--bloom-base) 100%); }
  .label--tide {
    background:
      linear-gradient(160deg, var(--tide-green) 0%, rgba(63,211,220,0) 22%),
      linear-gradient(200deg, var(--tide-deep) 0%, var(--tide-mid) 40%, var(--tide-light) 75%, var(--tide-mid) 100%);
  }
  .label__pattern { position: absolute; inset: 0; }

  .brand {
    position: absolute; top: 46px; left: 0; right: 0; text-align: center;
    font-family: "Montserrat", sans-serif; font-weight: 500;
    font-size: 27px; letter-spacing: 0.2em; text-transform: uppercase;
  }

  .flower { position: absolute; border-radius: 50%; filter: blur(2px); }
  .flower--bloom-top {
    left: -30px; top: 80px; width: 280px; height: 320px;
    background: radial-gradient(ellipse at 45% 50%, var(--bloom-flower) 0%, var(--bloom-flower-soft) 55%, rgba(255,95,184,0) 72%);
  }
  .flower--bloom-bottom {
    right: -40px; top: 470px; width: 260px; height: 360px;
    background: radial-gradient(ellipse at 55% 50%, var(--bloom-flower) 0%, var(--bloom-flower-soft) 55%, rgba(255,95,184,0) 72%);
  }
  .flower--orchid {
    left: -20px; top: 150px; width: 230px; height: 260px;
    background: radial-gradient(ellipse at 45% 50%, var(--orchid) 0%, var(--orchid-soft) 50%, rgba(183,154,208,0) 72%);
  }
  .flower--lily {
    right: -40px; top: 480px; width: 240px; height: 360px;
    background: radial-gradient(ellipse at 55% 50%, var(--white) 0%, var(--lily) 45%, rgba(232,184,228,0) 72%);
  }

  .name-frame {
    position: absolute; left: 22%; top: 36%; width: 56%; height: 22%;
    border: 1.5px solid var(--white);
  }
  .name-frame__fill {
    position: absolute; left: -6px; top: -6px; right: 6px; bottom: 6px;
  }
  .label--bloom .name-frame__fill { background: var(--bloom-box); }
  .label--tide .name-frame__fill { background: var(--tide-box); }
  .name-frame__title {
    position: absolute; inset: 0; display: flex; align-items: center; justify-content: center;
    text-align: center; font-family: "Oswald", sans-serif; font-weight: 200;
    font-size: 50px; line-height: 1.05; text-transform: uppercase; letter-spacing: -0.01em;
  }

  .type-box {
    position: absolute; left: 22%; top: 85%; width: 56%; height: 54px;
    border: 1.5px solid var(--white); text-align: center;
    font-family: "Montserrat", sans-serif; font-weight: 300;
  }
  .label--bloom .type-box { background: var(--bloom-box); }
  .label--tide .type-box { background: var(--tide-box); }
  .type-box__kind { display: block; font-size: 11px; letter-spacing: 0.28em; margin-top: 5px; font-weight: 400; }
  .type-box__product { display: block; font-size: 25px; line-height: 1.1; }

  .volume {
    position: absolute; top: 91.8%; left: 0; right: 0; text-align: center;
    font-family: "Montserrat", sans-serif; font-weight: 400; font-size: 19px;
  }
  .volume__mark { font-size: 22px; margin-right: 3px; }
</style>
</head>
<body>
<main class="sheet">

  <section class="label label--bloom">
    <div class="flower flower--bloom-top" role="img" aria-label="Photo of bright magenta azalea blossoms"></div>
    <div class="flower flower--bloom-bottom" role="img" aria-label="Photo of bright magenta azalea blossoms"></div>
    <p class="brand">Amber Drizzle</p>
    <div class="name-frame">
      <div class="name-frame__fill"></div>
      <h2 class="name-frame__title">Velvet<br>Petal</h2>
    </div>
    <div class="type-box">
      <span class="type-box__kind">FRAGANCE</span>
      <span class="type-box__product">BODY MIST</span>
    </div>
    <p class="volume"><span class="volume__mark">℮</span>250ml/8.4fl.oz</p>
  </section>

  <section class="label label--tide">
    <div class="label__pattern" role="img" aria-label="Flowing turquoise and blue brushstroke background"></div>
    <div class="flower flower--orchid" role="img" aria-label="Photo of pale lilac orchid flowers with dew drops"></div>
    <div class="flower flower--lily" role="img" aria-label="Photo of pink and white lily flowers"></div>
    <p class="brand">Amber Drizzle</p>
    <div class="name-frame">
      <div class="name-frame__fill"></div>
      <h2 class="name-frame__title">Coral<br>Tide</h2>
    </div>
    <div class="type-box">
      <span class="type-box__kind">FRAGANCE</span>
      <span class="type-box__product">BODY MIST</span>
    </div>
    <p class="volume"><span class="volume__mark">℮</span>250ml/8.4fl.oz</p>
  </section>

</main>
</body>
</html>
```